Update Veltrin & Co Powerpoint to Palewood Partnership

Hi, about 2 years ago I had a great Powerpoint template produced for my business called Veltrin & Co. We have now changed the company name and logo to Palewood Partnership and I would like you to update the presentation template pages to the new logo and design.

I attach:

1) The original Powerpoint presentation that was produced for Veltrin
2) The new Palewood Partnership logo files
3) The initial Powerpoint presentation format that my UK designer has done to give you an idea of their approach
4) The Font files (Red Hat Display - medium)

It would be great to receive the new PP template by Tuesday 22nd July.

Please message me if you have any questions.
Thanks
Ted

```html
<!DOCTYPE html>
<html lang="en">
<head>
<meta charset="utf-8">
<title>Palewood Partnership – Presentation Template</title>
<link rel="stylesheet" href="https://fonts.googleapis.com/css2?family=Red+Hat+Display:wght@400;500;700;800&family=Inter:wght@400;600;700&display=swap">
<style>
:root{
  --ink:#0f2a30;
  --accent:#d63f0e;
  --paper:#f3f6f9;
  --canvas:#ababab;
  --muted:#2b3a3f;
  --white:#ffffff;
}
*{box-sizing:border-box;margin:0;padding:0}
html,body{width:1012px;height:1200px;overflow:hidden}
body{background:var(--canvas);position:relative;font-family:"Inter",Arial,sans-serif;color:var(--muted)}

.slide{position:absolute;width:800px;height:450px;transform-origin:0 0;transform:scale(.57375);overflow:hidden;background:var(--paper)}
.slide-1{left:31.6px;top:37.9px}
.slide-2{left:520.9px;top:37.9px}
.slide-3{left:31.6px;top:326.4px}
.slide-4{left:520.9px;top:326.4px}
.slide-5{left:31.6px;top:615.6px}
.slide-6{left:520.9px;top:615.6px}
.slide-7{left:31.6px;top:904.2px}
.slide-8{left:520.9px;top:904.2px;background:var(--ink)}

.backdrop{position:absolute;inset:0;background:
  radial-gradient(ellipse 45% 40% at 45% 60%,rgba(190,160,140,.28),transparent 70%),
  linear-gradient(120deg,#f7f9fb 0%,#e7edf2 45%,#dfe6ec 70%,#eef2f5 100%)}
.slide-8 .backdrop{background:
  radial-gradient(ellipse 50% 45% at 45% 60%,rgba(60,90,95,.45),transparent 70%),
  linear-gradient(120deg,#12303a 0%,#0f2a30 60%,#0c242a 100%)}

.brand{position:absolute;left:67px;top:26px;display:flex;align-items:center;gap:7px}
.brand-mark{width:14px;height:14px;border-radius:50%;background:var(--accent);flex:none}
.brand-name{font-family:"Red Hat Display",Arial,sans-serif;font-weight:700;font-size:15px;line-height:1.05;color:var(--ink);width:84px}

.dots{position:absolute;display:flex;gap:6px}
.dots span{width:7px;height:7px;border-radius:50%;background:var(--ink)}
.dots span:nth-child(even){background:var(--accent)}
.dots-top{right:68px;top:30px}

.slide-title{position:absolute;right:68px;top:42px;font-family:"Red Hat Display",Arial,sans-serif;font-weight:700;font-size:22px;color:var(--ink)}

.footer-copy{position:absolute;left:67px;top:419px;font-size:9px;color:var(--ink)}
.footer-dots{left:375px;top:422px}
.footer-rule{position:absolute;left:480px;top:422px;width:252px;height:2px;background:var(--ink)}
.page-no{position:absolute;left:761px;top:414px;width:20px;height:20px;border-radius:50%;background:var(--accent);color:var(--white);font-size:7px;font-weight:700;display:flex;align-items:center;justify-content:center}

.body-text{position:absolute;font-size:9px;line-height:1.42;text-align:justify;color:var(--muted)}
.body-text p+p{margin-top:10px}

.photo{position:absolute;background:linear-gradient(135deg,#6d7c82 0%,#b9b2a7 45%,#8b8a86 100%)}

/* Cover */
.cover-brand{position:absolute;left:70px;top:86px;display:flex;align-items:center;gap:10px}
.cover-brand .brand-mark{width:26px;height:26px}
.cover-brand .brand-name{font-size:28px;width:auto}
.cover-bar{position:absolute;left:70px;top:208px;width:4px;height:104px;background:var(--accent)}
.cover-title{position:absolute;left:92px;top:198px;font-family:"Red Hat Display",Arial,sans-serif;font-size:56px;line-height:1.07;color:var(--ink)}
.cover-title strong{font-weight:800;display:block}
.cover-title span{font-weight:400;display:block}
.cover-sub{position:absolute;left:70px;top:326px;width:330px;font-size:10.5px;line-height:1.5;color:var(--ink)}

/* Features */
.feature-hub{position:absolute;left:480px;top:208px;width:36px;height:36px;background:var(--accent);transform:rotate(45deg)}
.feature-icon{position:absolute;width:60px;height:60px;border-radius:50%;background:var(--ink);display:flex;align-items:center;justify-content:center}
.feature-text{position:absolute;width:130px;font-size:9px;font-weight:700;line-height:1.4;color:var(--ink)}
.feature-text.left{text-align:right}

/* Agenda list */
.agenda-item{position:absolute;width:258px;height:40px}
.diamond{position:absolute;left:0;top:0;width:26px;height:26px;background:var(--accent);transform:rotate(45deg)}
.diamond-no{position:absolute;left:0;top:0;width:26px;height:26px;display:flex;align-items:center;justify-content:center;color:var(--white);font-size:9px;font-weight:700}
.agenda-text{position:absolute;left:36px;top:-6px;width:232px;font-size:10px;line-height:1.55;color:var(--ink)}
.agenda-rule{position:absolute;left:36px;top:28px;width:232px;height:2px;background:var(--ink)}

.dark-panel{position:absolute;left:67px;top:100px;width:392px;height:290px;background:var(--ink)}
.dark-panel .agenda-text{color:var(--white)}

/* Chart */
.chart{position:absolute;left:60px;top:100px}
.chart text{font-family:"Inter",Arial,sans-serif;font-size:8px;fill:var(--ink)}
.stat{position:absolute;left:445px;width:260px;height:50px}
.stat-icon{position:absolute;left:0;top:0;width:46px;height:46px;border-radius:50%;background:var(--accent);border:3px solid var(--ink);display:flex;align-items:center;justify-content:center}
.stat-title{position:absolute;left:58px;top:0;font-size:10px;font-weight:700;color:var(--ink)}
.stat-body{position:absolute;left:58px;top:17px;width:200px;font-size:8px;line-height:1.5;color:var(--muted)}

/* Offer */
.offer-photo{top:95px;width:142px;height:145px}
.offer-badge{position:absolute;top:228px;width:24px;height:24px;border-radius:50%;background:var(--white);border:2px solid var(--accent)}

/* Closing */
.closing-brand{position:absolute;left:0;right:0;top:86px;display:flex;justify-content:center;align-items:center;gap:8px}
.closing-brand .brand-name{color:var(--white);width:auto;font-size:17px}
.closing-dots{left:364px;top:186px;gap:8px}
.closing-dots span,.slide-8 .footer-dots span{background:var(--accent)}
.closing-dots span{width:12px;height:12px}
.closing-title{position:absolute;left:0;right:0;top:196px;text-align:center;font-family:"Red Hat Display",Arial,sans-serif;font-weight:800;font-size:82px;color:var(--white)}
.slide-8 .footer-copy{color:var(--white)}
.slide-8 .footer-rule{background:var(--white)}
</style>
</head>
<body>

<!-- Cover -->
<section class="slide slide-1">
  <div class="backdrop" role="img" aria-label="Faint photo of a business handshake over a city skyline"></div>
  <div class="dots dots-top"><span></span><span></span><span></span><span></span></div>
  <div class="cover-brand"><div class="brand-mark"></div><div class="brand-name">Palewood Partnership</div></div>
  <div class="cover-bar"></div>
  <h1 class="cover-title"><strong>Palewood</strong><span>Partnership</span></h1>
  <p class="cover-sub">Lorem ipsum dolor sit amet, consectetur adipiscing elit, sed do tempor incididunt ut labore et dolore magna aliqua.</p>
  <div class="dots" style="left:70px;top:396px"><span></span><span></span><span></span><span></span></div>
</section>

<!-- Features -->
<section class="slide slide-2">
  <div class="backdrop" role="img" aria-label="Faint photo of a business handshake over a city skyline"></div>
  <div class="brand"><div class="brand-mark"></div><div class="brand-name">Palewood Partnership</div></div>
  <div class="dots dots-top"><span></span><span></span><span></span><span></span></div>
  <h2 class="slide-title">Title Here</h2>
  <div class="body-text" style="left:67px;top:100px;width:176px">
    <p>Lorem ipsum dolor sit amet, consectetur adipiscing elit, sed do eiusmod tempor incididunt ut labore et dolore magna aliqua. Ut enim ad minim veniam, quis nostrud exercitation ullamco laboris nisi ut aliquip ex ea commodo consequat. Duis aute irure dolor in reprehenderit in voluptate velit esse cillum dolore eu fugiat nulla pariatur. Excepteur sint occaecat cupidatat non proident, sunt in culpa qui officia deserunt mollit anim id est laborum.</p>
    <p>Sed ut perspiciatis unde omnis iste natus error sit voluptatem accusantium dolore mque laudantium, totam rem aperiam, eaque ipsa quae ab illo inventore veritatis et quasi architecto beatae vitae dicta sunt explicabo. Nemo enim ipsam voluptatem quia voluptas sit aspernatur aut odit aut fugit, sed quia consequuntur</p>
  </div>
  <div class="feature-hub"></div>
  <div class="feature-icon" style="left:403px;top:133px"><svg width="28" height="28" viewBox="0 0 28 28" fill="none" stroke="#fff" stroke-width="1.4"><path d="M3 14l6-5 5 3 5-3 6 5-6 6-5-3-5 3z"/><path d="M9 9l5 4"/></svg></div>
  <div class="feature-icon" style="left:536px;top:133px"><svg width="28" height="28" viewBox="0 0 28 28" fill="none" stroke="#fff" stroke-width="1.4"><rect x="4" y="5" width="18" height="13"/><path d="M8 15v-3M12 15v-5M16 15v-2"/><circle cx="20" cy="18" r="3.5"/><path d="M22.5 20.5l3 3"/></svg></div>
  <div class="feature-icon" style="left:403px;top:259px"><svg width="28" height="28" viewBox="0 0 28 28" fill="none" stroke="#fff" stroke-width="1.4"><path d="M4 24h20M7 24v-6M12 24v-9M17 24v-7M22 24v-12M6 14l6-5 4 3 7-6"/></svg></div>
  <div class="feature-icon" style="left:536px;top:259px"><svg width="28" height="28" viewBox="0 0 28 28" fill="none" stroke="#fff" stroke-width="1.4"><circle cx="14" cy="9" r="3"/><circle cx="6" cy="19" r="3"/><circle cx="22" cy="19" r="3"/><path d="M12 11l-4 6M16 11l4 6M9 19h10"/></svg></div>
  <p class="feature-text left" style="left:265px;top:144px">Lorem ipsum dolor sit ame consectetur adipisc ing elit, sedaliqua.</p>
  <p class="feature-text" style="left:606px;top:144px">Lorem ipsum dolor sit ame consectetur adipisc ing elit, sedaliqua.</p>
  <p class="feature-text left" style="left:265px;top:270px">Lorem ipsum dolor sit ame consectetur adipisc ing elit, sedaliqua.</p>
  <p class="feature-text" style="left:606px;top:270px">Lorem ipsum dolor sit ame consectetur adipisc ing elit, sedaliqua.</p>
  <p class="footer-copy">© Copyrights 2025 I All Rights Reserved</p>
  <div class="dots footer-dots"><span></span><span></span><span></span><span></span></div>
  <div class="footer-rule"></div>
  <div class="page-no">05</div>
</section>

<!-- Agenda -->
<section class="slide slide-3">
  <div class="backdrop" role="img" aria-label="Faint photo of a business handshake over a city skyline"></div>
  <div class="brand"><div class="brand-mark"></div><div class="brand-name">Palewood Partnership</div></div>
  <div class="dots dots-top"><span></span><span></span><span></span><span></span></div>
  <h2 class="slide-title">Agenda</h2>
  <div class="agenda-item" style="left:101px;top:118px"><div class="diamond"></div><div class="diamond-no">01</div><p class="agenda-text">Lorem ipsum dolor sit amet, consectetur adipiscing elit, ut labore et dolore magna aliqua.</p><div class="agenda-rule"></div></div>
  <div class="agenda-item" style="left:101px;top:192px"><div class="diamond"></div><div class="diamond-no">02</div><p class="agenda-text">Lorem ipsum dolor sit amet, consectetur adipiscing elit, ut labore et dolore magna aliqua.</p><div class="agenda-rule"></div></div>
  <div class="agenda-item" style="left:101px;top:266px"><div class="diamond"></div><div class="diamond-no">03</div><p class="agenda-text">Lorem ipsum dolor sit amet, consectetur adipiscing elit, ut labore et dolore magna aliqua.</p><div class="agenda-rule"></div></div>
  <div class="agenda-item" style="left:101px;top:340px"><div class="diamond"></div><div class="diamond-no">04</div><p class="agenda-text">Lorem ipsum dolor sit amet, consectetur adipiscing elit, ut labore et dolore magna aliqua.</p><div class="agenda-rule"></div></div>
  <div class="agenda-item" style="left:426px;top:118px"><div class="diamond"></div><div class="diamond-no">05</div><p class="agenda-text">Lorem ipsum dolor sit amet, consectetur adipiscing elit, ut labore et dolore magna aliqua.</p><div class="agenda-rule"></div></div>
  <div class="agenda-item" style="left:426px;top:192px"><div class="diamond"></div><div class="diamond-no">06</div><p class="agenda-text">Lorem ipsum dolor sit amet, consectetur adipiscing elit, ut labore et dolore magna aliqua.</p><div class="agenda-rule"></div></div>
  <div class="agenda-item" style="left:426px;top:266px"><div class="diamond"></div><div class="diamond-no">07</div><p class="agenda-text">Lorem ipsum dolor sit amet, consectetur adipiscing elit, ut labore et dolore magna aliqua.</p><div class="agenda-rule"></div></div>
  <div class="agenda-item" style="left:426px;top:340px"><div class="diamond"></div><div class="diamond-no">08</div><p class="agenda-text">Lorem ipsum dolor sit amet, consectetur adipiscing elit, ut labore et dolore magna aliqua.</p><div class="agenda-rule"></div></div>
  <div class="dots footer-dots"><span></span><span></span><span></span><span></span></div>
  <div class="page-no">02</div>
</section>

<!-- List with photo -->
<section class="slide slide-4">
  <div class="backdrop" role="img" aria-label="Faint photo of a business handshake over a city skyline"></div>
  <div class="brand"><div class="brand-mark"></div><div class="brand-name">Palewood Partnership</div></div>
  <div class="dots dots-top"><span></span><span></span><span></span><span></span></div>
  <h2 class="slide-title">Title Here</h2>
  <div class="dark-panel">
    <div class="agenda-item" style="left:30px;top:34px"><div class="diamond"></div><div class="diamond-no">01</div><p class="agenda-text">Lorem ipsum dolor sit amet, consectetur adipiscing elit, ut labore et dolore magna aliqua.</p></div>
    <div class="agenda-item" style="left:30px;top:98px"><div class="diamond"></div><div class="diamond-no">02</div><p class="agenda-text">Lorem ipsum dolor sit amet, consectetur adipiscing elit, ut labore et dolore magna aliqua.</p></div>
    <div class="agenda-item" style="left:30px;top:162px"><div class="diamond"></div><div class="diamond-no">03</div><p class="agenda-text">Lorem ipsum dolor sit amet, consectetur adipiscing elit, ut labore et dolore magna aliqua.</p></div>
    <div class="agenda-item" style="left:30px;top:226px"><div class="diamond"></div><div class="diamond-no">04</div><p class="agenda-text">Lorem ipsum dolor sit amet, consectetur adipiscing elit, ut labore et dolore magna aliqua.</p></div>
  </div>
  <div class="photo" style="left:400px;top:121px;width:332px;height:248px" role="img" aria-label="Photo of a presenter at a wall screen in a brick-walled meeting room with seated colleagues"></div>
  <p class="footer-copy">© Copyrights 2025 I All Rights Reserved</p>
  <div class="dots footer-dots"><span></span><span></span><span></span><span></span></div>
  <div class="footer-rule"></div>
  <div class="page-no">06</div>
</section>

<!-- About -->
<section class="slide slide-5">
  <div class="backdrop" role="img" aria-label="Faint photo of a business handshake over a city skyline"></div>
  <div class="brand"><div class="brand-mark"></div><div class="brand-name">Palewood Partnership</div></div>
  <div class="dots dots-top"><span></span><span></span><span></span><span></span></div>
  <h2 class="slide-title">About Us</h2>
  <div class="body-text" style="left:67px;top:120px;width:318px">
    <p>Lorem ipsum dolor sit amet, consectetur adipiscing elit, sed do eiusmod tempor incididunt ut labore et dolore magna aliqua. Ut enim ad minim veniam, quis nostrud exercitation ullamco laboris nisi ut aliquip ex ea commodo consequat. Duis aute irure dolor in reprehenderit in voluptate velit esse cillum dolore eu fugiat nulla pariatur. Excepteur sint occaecat cupidatat non proident, sunt in culpa qui officia deserunt mollit anim id est laborum.</p>
    <p>Sed ut perspiciatis unde omnis iste natus error sit voluptatem accusantium doloremque laudantium, totam rem aperiam, eaque ipsa quae ab illo inventore veritatis et quasi architecto beatae vitae dicta sunt explicabo. Nemo enim ipsam voluptatem quia voluptas sit aspernatur aut odit aut fugit, sed quia consequuntur magni dolores eos qui ratione voluptatem sequi nesciunt. Neque porro quisquam est, qui dolorem ipsum quia dolor sit amet, consectetur, adipisci velit, sed quia non numquam eius modi tempora incidunt ut labore et dolore magnam aliquam quaerat voluptatem. Ut enim ad minima veniam, quis nostrum exercitationem ullam corporis suscipit laboriosam, nisi ut aliquid ex ea commodi consequatur? Quis autem vel eum iure reprehenderit qui in ea voluptate velit esse quam nihil molestiae consequatur, vel illum qui dolorem eum fugiat quo voluptas nulla pariatur</p>
  </div>
  <div style="position:absolute;left:408px;top:91px;width:101px;height:292px;background:var(--accent)"></div>
  <div class="photo" style="left:433px;top:116px;width:299px;height:242px" role="img" aria-label="Photo of a team discussing plans around a table in a loft office"></div>
  <p class="footer-copy">© Copyrights 2025 I All Rights Reserved</p>
  <div class="dots footer-dots"><span></span><span></span><span></span><span></span></div>
  <div class="footer-rule"></div>
  <div class="page-no">03</div>
</section>

<!-- Chart -->
<section class="slide slide-6">
  <div class="backdrop" role="img" aria-label="Faint photo of a business handshake over a city skyline"></div>
  <div class="brand"><div class="brand-mark"></div><div class="brand-name">Palewood Partnership</div></div>
  <div class="dots dots-top"><span></span><span></span><span></span><span></span></div>
  <h2 class="slide-title">Title Here</h2>
  <svg class="chart" width="330" height="280" viewBox="0 0 330 280">
    <line x1="35" y1="10" x2="35" y2="260" stroke="#b9c2c7" stroke-width="1"/>
    <g text-anchor="end">
      <text x="20" y="263">0</text><text x="20" y="238">1</text><text x="20" y="213">2</text><text x="20" y="188">3</text><text x="20" y="163">4</text><text x="20" y="138">5</text><text x="20" y="113">6</text><text x="20" y="88">7</text><text x="20" y="63">8</text><text x="20" y="38">9</text><text x="20" y="13">10</text>
    </g>
    <rect x="57" y="147.5" width="18" height="112.5" fill="#0f2a30"/>
    <rect x="105" y="135" width="18" height="125" fill="#d63f0e"/>
    <rect x="152" y="82.5" width="18" height="177.5" fill="#0f2a30"/>
    <rect x="200" y="135" width="18" height="125" fill="#d63f0e"/>
    <rect x="248" y="147.5" width="18" height="112.5" fill="#0f2a30"/>
    <rect x="296" y="82.5" width="18" height="177.5" fill="#d63f0e"/>
    <g text-anchor="middle" font-size="7">
      <text x="66" y="142">4.5%</text><text x="114" y="129">5%</text><text x="161" y="77">7.1%</text><text x="209" y="129">5%</text><text x="257" y="142">4.5%</text><text x="305" y="77">7.1%</text>
    </g>
    <g text-anchor="middle">
      <text x="66" y="274">2000</text><text x="114" y="274">2005</text><text x="161" y="274">2010</text><text x="209" y="274">2015</text><text x="257" y="274">2020</text><text x="305" y="274">2024</text>
    </g>
  </svg>
  <div class="stat" style="top:106px"><div class="stat-icon"><svg width="20" height="20" viewBox="0 0 20 20" fill="none" stroke="#fff" stroke-width="1.3"><circle cx="6" cy="7" r="2.5"/><circle cx="14" cy="7" r="2.5"/><path d="M2 17c0-3 2-5 4-5s4 2 4 5M10 17c0-3 2-5 4-5s4 2 4 5"/></svg></div><p class="stat-title">Lorem ipsum dolor sit amet</p><p class="stat-body">Lorem ipsum dolor sit amet, consectetur adipiscing elit, sed do eiusmod tempor incididunt ut</p></div>
  <div class="stat" style="top:178px"><div class="stat-icon"><svg width="20" height="20" viewBox="0 0 20 20" fill="none" stroke="#fff" stroke-width="1.3"><circle cx="10" cy="10" r="6"/><circle cx="10" cy="10" r="2.5"/><path d="M10 2v2M10 16v2M2 10h2M16 10h2"/></svg></div><p class="stat-title">Lorem ipsum dolor sit amet</p><p class="stat-body">Lorem ipsum dolor sit amet, consectetur adipiscing elit, sed do eiusmod tempor incididunt ut</p></div>
  <div class="stat" style="top:251px"><div class="stat-icon"><svg width="20" height="20" viewBox="0 0 20 20" fill="none" stroke="#fff" stroke-width="1.3"><path d="M4 3h12v5a6 6 0 0 1-12 0z"/><path d="M10 14v3M6 17h8"/></svg></div><p class="stat-title">Lorem ipsum dolor sit amet</p><p class="stat-body">Lorem ipsum dolor sit amet, consectetur adipiscing elit, sed do eiusmod tempor incididunt ut</p></div>
  <div class="stat" style="top:323px"><div class="stat-icon"><svg width="20" height="20" viewBox="0 0 20 20" fill="none" stroke="#fff" stroke-width="1.3"><circle cx="10" cy="10" r="7"/><path d="M6 10l3 3 5-6"/></svg></div><p class="stat-title">Lorem ipsum dolor sit amet</p><p class="stat-body">Lorem ipsum dolor sit amet, consectetur adipiscing elit, sed do eiusmod tempor incididunt ut</p></div>
  <p class="footer-copy">© Copyrights 2025 I All Rights Reserved</p>
  <div class="dots footer-dots"><span></span><span></span><span></span><span></span></div>
  <div class="footer-rule"></div>
  <div class="page-no">07</div>
</section>

<!-- Offer -->
<section class="slide slide-7">
  <div class="backdrop" role="img" aria-label="Faint photo of a business handshake over a city skyline"></div>
  <div class="brand"><div class="brand-mark"></div><div class="brand-name">Palewood Partnership</div></div>
  <div class="dots dots-top"><span></span><span></span><span></span><span></span></div>
  <h2 class="slide-title">What We Offer</h2>
  <div class="body-text" style="left:67px;top:100px;width:176px">
    <p>Lorem ipsum dolor sit amet, consectetur adipiscing elit, sed do eiusmod tempor incididunt ut labore et dolore magna aliqua. Ut enim ad minim veniam, quis nostrud exercitation ullamco laboris nisi ut aliquip ex ea commodo consequat. Duis aute irure dolor in reprehenderit in voluptate velit esse cillum dolore eu fugiat nulla pariatur. Excepteur sint occaecat cupidatat non proident, sunt in culpa qui officia deserunt mollit anim id est laborum.</p>
    <p>Sed ut perspiciatis unde omnis iste natus error sit voluptatem accusantium dolore mque laudantium, totam rem aperiam, eaque ipsa quae ab illo inventore veritatis et quasi architecto beatae vitae dicta sunt explicabo. Nemo enim ipsam voluptatem quia voluptas sit aspernatur aut odit aut fugit, sed quia consequuntur</p>
  </div>
  <div class="photo offer-photo" style="left:278px" role="img" aria-label="Photo of a man presenting from a laptop in a dim office"></div>
  <div class="photo offer-photo" style="left:434px" role="img" aria-label="Photo of colleagues celebrating at their desks"></div>
  <div class="photo offer-photo" style="left:590px" role="img" aria-label="Photo of three colleagues looking at a laptop together"></div>
  <div class="offer-badge" style="left:337px"></div>
  <div class="offer-badge" style="left:493px"></div>
  <div class="offer-badge" style="left:649px"></div>
  <p class="body-text" style="left:278px;top:262px;width:142px">Lorem ipsum dolor sit amet, consectetur adipiscing elit, sed do eiusmod tempor incididunt ut labore et dolore magna aliqua. Ut enim ad minim veniam, quis nostrud exercitation ullamco laboris nisi ut aliquip ex ea commodo consequat.</p>
  <p class="body-text" style="left:434px;top:262px;width:142px">Lorem ipsum dolor sit amet, consectetur adipiscing elit, sed do eiusmod tempor incididunt ut labore et dolore magna aliqua. Ut enim ad minim veniam, quis nostrud exercitation ullamco laboris nisi ut aliquip ex ea commodo consequat.</p>
  <p class="body-text" style="left:590px;top:262px;width:142px">Lorem ipsum dolor sit amet, consectetur adipiscing elit, sed do eiusmod tempor incididunt ut labore et dolore magna aliqua. Ut enim ad minim veniam, quis nostrud exercitation ullamco laboris nisi ut aliquip ex ea commodo consequat.</p>
  <p class="footer-copy">© Copyrights 2025 I All Rights Reserved</p>
  <div class="dots footer-dots"><span></span><span></span><span></span><span></span></div>
  <div class="footer-rule"></div>
  <div class="page-no">04</div>
</section>

<!-- Closing -->
<section class="slide slide-8">
  <div class="backdrop" role="img" aria-label="Dark-toned photo of a business handshake over a city skyline"></div>
  <div class="closing-brand"><div class="brand-mark"></div><div class="brand-name">Palewood Partnership</div></div>
  <div class="dots closing-dots"><span></span><span></span><span></span><span></span></div>
  <h2 class="closing-title">Thank You</h2>
  <p class="footer-copy">© Copyrights 2025 I All Rights Reserved</p>
  <div class="dots footer-dots"><span></span><span></span><span></span><span></span></div>
  <div class="footer-rule"></div>
  <div class="page-no">08</div>
</section>

</body>
</html>
```